Seafood Retailer requires varies packaging labels

We are an established business (Restaurant, Seafood Retailer and Crayfish Wholesaler). We have just got a new logo which covers all three aspects of our business (via Artbazaar!). We have always sold cellar door but have been asked by several food outlets to stock our product but as you will see from our pictures - it needs some serious work to take us to the next level. We have a well known finer dining restaurant which we use all these products in and is how several products came about on our Seafood shop shelves. The products are of high quality (just not the labelling). We now want to package our Seafood Retail Shop with professional packaging and labelling and reflect the "quality and freshness" of our products. We have several items we want to label as per below.

If we were to use a slogan it would be "Its about the Freshness and Quality" but not necessary.

We are after a label for our Pickled Seafood 350g tub (Various) - conical container 9cm high x 9cm (top), 7cm (bottom) ONLY but will also try and utilise it to be consistent with the other products following.

Salt and Pepper MIx 250g - conical container (as above)
Smoked Fish (Various weight & fish) - 21cm x 25cm vacuum sealed bags.
Kilpatrick Sauce 250ml - square bottle 22cm high x 4.5cm wide
Minty Lime Vinaigrette 250ml - 23cm round bottle - 4.7cm dia.
Smoked Spicy Salt 75g- 13cm wide x 16cm high vacuum bag
Dukkah 75g - 13cm wide x 16cm high vacuum bag
Lobster Oil 150ml - 18cm x 4.5cm dia round bottle

We will need a working file so we can change the names for the pickled seafood as needed.

I have attached photos of our current products for true understanding of what we currently have had to get by and where we wish to go.

We have a label printer that can print black type overs eg the name of each product so we can have generic coloured labels which we can print over with the change of each product.

We want something that will become a recognisable label.
Updates

Attn Designers.
We are only after one design but which we will use as a guide for all the options supplied as a starting point. The Pickled containers will probably be where we start but happy with any submissions. I probably wasnt very clear but wanted to show all the things we will be using the labelling for so that we can get some continuity We are just after some direction on a good look.  Thanks Marlo

Reason: Had some technical problems and wish to extend the time to allow more time conversing with designers.

Target Market(s)

Our target market varies but generally 30 - 65 years in the more affluent background. We are located "literally in the middle of a paddock in the middle of nowhere" (near several holiday villages) and it is the reputation of our premium, fresh products that have people returning and amazed on their first experience.

Industry/Entity Type

Restaurant

Requirements
Must have
• All:

Our logo and the colours are:
Orange
C 13%
M 79%
Y 100%
K 3%

Blue
C 100%
M 96%
Y 14%
K 3%

weight

nutrition panel, barcode (but we can also do that as a separate label on the back ourselves if needed)

"Produced & packaged by:
Harbourline Catch Pty Ltd, 40731 Pellam Highway, Tondarra SA 5592
Ph: 08 86120394"

Made in Australia from local and imported ingredients. Keep refrigerated. Store at 1oC - 4oC. Use in 7 days after opening.

Nice to have
• Pickled seafood - "Gourmet Pickled" and "Ready to Eat"
Should not have
• Use only the "Harbourline Catch" logo (not the "harbourline Restaurant & Seafood Sales or Restaurant Only logos)

```html
<!DOCTYPE html>
<html lang="en">
<head>
<meta charset="utf-8">
<title>Harbourline Catch – Pickled Seafood Labels</title>
<link href="https://fonts.googleapis.com/css2?family=Lobster&family=Montserrat:wght@600;700&display=swap" rel="stylesheet">
<style>
  :root {
    --backdrop: #808285;
    --navy: #2e3184;
    --orange: #c8541f;
    --orange-dark: #9c3b14;
    --sky-light: #dcecf8;
    --sky-mid: #8fc0e6;
    --sky-deep: #4f95d2;
    --wave-light: #9fdcf0;
    --wave-deep: #1f8fbf;
    --white: #ffffff;
    --ink: #2b2b2b;
  }
  html, body {
    margin: 0;
    padding: 0;
    width: 1019px;
    height: 1200px;
    overflow: hidden;
    background: var(--backdrop);
  }
  .label-sheet { display: block; width: 1019px; height: 1200px; }
  .brand-name {
    font-family: "Montserrat", sans-serif;
    font-weight: 700;
    fill: var(--navy);
    letter-spacing: 1px;
  }
  .product-title {
    font-family: "Lobster", cursive;
    fill: var(--white);
    stroke: var(--navy);
    stroke-width: 7px;
    paint-order: stroke;
    stroke-linejoin: round;
  }
  .variety-name {
    font-family: "Montserrat", sans-serif;
    font-weight: 700;
    fill: var(--ink);
    font-size: 21px;
    letter-spacing: 1px;
  }
  .net-weight {
    font-family: "Montserrat", sans-serif;
    font-weight: 700;
    fill: var(--navy);
    font-size: 20px;
  }
  .storage-note {
    font-family: "Montserrat", sans-serif;
    font-weight: 600;
    fill: var(--white);
    font-size: 14.5px;
  }
  .producer-details {
    font-family: "Montserrat", sans-serif;
    font-weight: 600;
    fill: var(--white);
    font-size: 9.6px;
  }
</style>
</head>
<body>
<svg class="label-sheet" viewBox="0 0 1019 1200" xmlns="http://www.w3.org/2000/svg">
  <defs>
    <radialGradient id="sky-burst" cx="50%" cy="45%" r="70%">
      <stop offset="0" stop-color="var(--sky-light)"/>
      <stop offset="0.55" stop-color="var(--sky-mid)"/>
      <stop offset="1" stop-color="var(--sky-deep)"/>
    </radialGradient>
    <linearGradient id="surf" x1="0" y1="0" x2="0" y2="1">
      <stop offset="0" stop-color="var(--wave-light)"/>
      <stop offset="1" stop-color="var(--wave-deep)"/>
    </linearGradient>
    <clipPath id="lid-clip"><circle cx="510" cy="365" r="283"/></clipPath>
    <path id="title-arc" d="M105 905 Q330 775 560 905"/>
  </defs>

  <!-- Lid label -->
  <g class="lid-label">
    <circle cx="510" cy="365" r="288" fill="url(#sky-burst)"/>
    <g clip-path="url(#lid-clip)">
      <rect role="img" aria-label="Crashing ocean wave illustration with foam bubbles" x="200" y="385" width="620" height="270" fill="url(#surf)"/>
    </g>
    <circle cx="510" cy="365" r="288" fill="none" stroke="var(--navy)" stroke-width="10"/>
    <circle cx="355" cy="222" r="9" fill="var(--orange)"/>
    <text class="brand-name" x="375" y="232" font-size="30">HARBOURLINE CATCH</text>
    <text class="product-title" x="502" y="347" font-size="66" text-anchor="middle">Pickled Seafood</text>
  </g>

  <!-- Front label -->
  <g class="front-label">
    <rect x="27" y="700" width="602" height="468" fill="url(#sky-burst)"/>
    <rect role="img" aria-label="Crashing ocean wave illustration with foam bubbles" x="27" y="960" width="602" height="183" fill="url(#surf)"/>
    <circle cx="205" cy="755" r="8" fill="var(--orange)"/>
    <text class="brand-name" x="222" y="764" font-size="26">HARBOURLINE CATCH</text>
    <text class="product-title" font-size="56"><textPath href="#title-arc">Pickle Seafood</textPath></text>
    <path d="M128 1055 L128 975 Q128 905 326 905 Q524 905 524 975 L524 1055 Z" fill="var(--white)" stroke="var(--orange)" stroke-width="6"/>
    <polygon points="82,1042 124,1042 124,1094 82,1094 98,1068" fill="var(--orange-dark)"/>
    <polygon points="570,1042 528,1042 528,1094 570,1094 554,1068" fill="var(--orange-dark)"/>
    <rect x="104" y="1050" width="444" height="38" fill="var(--orange)"/>
    <text class="variety-name" x="326" y="1077" text-anchor="middle">CALAMARI</text>
    <text class="net-weight" x="326" y="1125" text-anchor="middle">350g</text>
    <rect x="27" y="1143" width="602" height="25" fill="var(--navy)"/>
    <text class="storage-note" x="328" y="1161" text-anchor="middle">Keep refrigerated. Store at 1°C - 4°C. Use in 7 days after opening</text>
  </g>

  <!-- Back label -->
  <g class="back-label">
    <rect x="660" y="700" width="331" height="468" fill="url(#sky-burst)"/>
    <rect role="img" aria-label="Crashing ocean wave illustration with foam bubbles" x="660" y="1040" width="331" height="128" fill="url(#surf)"/>
    <rect x="674" y="745" width="304" height="333" rx="22" fill="var(--navy)" stroke="var(--white)" stroke-width="5"/>
    <rect x="715" y="767" width="220" height="230" rx="16" fill="var(--white)"/>
    <text class="producer-details" text-anchor="middle">
      <tspan x="826" y="1017">Made in Australia from local and imported ingredients.</tspan>
      <tspan x="826" y="1030">Produced &amp; packaged by:</tspan>
      <tspan x="826" y="1043">Harbourline Catch Pty Ltd, 40731 Pellam Highway,</tspan>
      <tspan x="826" y="1056">Tondarra SA 5592</tspan>
      <tspan x="826" y="1069">Ph: 08 86120394</tspan>
    </text>
    <rect x="762" y="1091" width="130" height="60" fill="var(--white)"/>
  </g>
</svg>
</body>
</html>
```